Verpackungsdesign für Glasprodukte
Zielgruppe
Wir sind eine Glaser Handwerksunternehmen die Dienstleistung und Glasprodukte verkaufen, unsere Zielgruppe sind BtoB und BtoC Kunden an die wir hochwertige Produkte für faire Preise anbieten.
Aufgabenstellung
Schlichtes und modernes Design, auf der Vorderseite soll das Logo, innen kommt eine Persönlicher Text und ein Bild von mir

```html
<!DOCTYPE html>
<html lang="de">
<head>
<meta charset="utf-8">
<title>Glaserei Velmar – Verpackung Innenseite</title>
<link rel="stylesheet" href="https://fonts.googleapis.com/css2?family=Open+Sans:wght@400;700&display=swap">
<style>
  :root {
    --cream: #f6ecc8;
    --cream-light: #fbf5de;
    --gold: #c9a66b;
    --gold-deep: #9c7443;
    --shadow-slate: #4a4c45;
    --ink: #1c1b18;
    --icon-ink: #6a5a48;
    --brand: #8a6a3f;
    --photo-dark: #2c3033;
    --photo-light: #c9cbcc;
  }
  * { box-sizing: border-box; margin: 0; padding: 0; }
  html, body { width: 1200px; height: 673px; overflow: hidden; background: var(--cream); }
  .packaging {
    position: relative;
    width: 1200px;
    height: 673px;
    overflow: hidden;
    font-family: "Open Sans", Arial, sans-serif;
    color: var(--ink);
  }
  .backdrop {
    position: absolute; inset: 0;
    background:
      radial-gradient(ellipse 40% 35% at 5% 100%, var(--shadow-slate) 0%, rgba(74,76,69,0) 100%),
      radial-gradient(ellipse 40% 35% at 95% 100%, var(--shadow-slate) 0%, rgba(74,76,69,0) 100%),
      radial-gradient(ellipse 25% 30% at 10% 55%, var(--gold-deep) 0%, rgba(156,116,67,0) 100%),
      radial-gradient(ellipse 25% 30% at 90% 55%, var(--gold-deep) 0%, rgba(156,116,67,0) 100%),
      radial-gradient(ellipse 60% 60% at 50% 45%, var(--cream-light) 0%, var(--cream) 55%, var(--gold) 100%);
  }
  .portrait {
    position: absolute; left: 405px; top: 100px; width: 186px; height: 280px;
    background: linear-gradient(90deg, var(--photo-dark) 0%, #4a4f52 45%, var(--photo-light) 100%);
  }
  .bio {
    position: absolute; left: 613px; top: 98px; width: 164px;
    font-size: 7px; line-height: 9.3px;
  }
  .bio h2 { font-size: 7px; font-weight: 700; line-height: 9.3px; margin-bottom: 9.3px; }
  .bio p { text-align: justify; margin-bottom: 9.3px; letter-spacing: -0.05px; }
  .contact {
    position: absolute; left: 418px; top: 433px; font-size: 9.6px; line-height: 12px; font-style: normal;
  }
  .contact .row { position: relative; padding-left: 20px; }
  .contact .icon { position: absolute; left: 0; top: 1px; }
  .contact .address { margin-top: 11px; font-size: 9px; line-height: 11px; }
  .contact .mail { margin-top: 11px; font-size: 9px; }
  .contact .web { margin-top: 11px; }
  .social { position: absolute; left: 612px; top: 431px; }
  .social .channel { display: flex; align-items: center; gap: 6px; height: 33px; margin-bottom: 6px; font-size: 9px; }
  .social .square { width: 33px; height: 33px; background: var(--brand); }
  .brand-name {
    position: absolute; left: 936px; top: 152px; width: 126px;
    color: var(--brand); font-size: 16px; font-weight: 400; line-height: 20px; text-align: center;
  }
</style>
</head>
<body>
<main class="packaging">
  <div class="backdrop" role="img" aria-label="Polygonmuster in Creme- und Goldtönen"></div>

  <div class="portrait" role="img" aria-label="Porträtfoto des Geschäftsführers mit verschränkten Armen"></div>

  <section class="bio">
    <h2>Geschäftsführer</h2>
    <h2>Lukas-Henrik Velmar</h2>
    <p>adipiscing elit. Aenean commodo ligula eget dolor. Aenean massa. Cum sociis natoque penatibus et magnis dis parturient montes, nascetur ridiculus mus. Donec quam felis, ultricies nec, pellentesque eu, pretium quis, sem. Nulla consequat massa quis enim. Donec pede justo, fringilla vel, aliquet nec, vulputate eget, arcu. In enim justo, rhoncus ut, imperdiet a, venenatis vitae, justo. Nullam dictum felis eu pede mollis pretium. Integer tincidunt. Cras dapibus. Vivamus elementum semper nisi. Aenean vulputate eleifend tellus. Aenean leo ligula, porttitor eu, consequat vitae, eleifend ac, enim. Aliquam lorem ante, dapibus in, viverra quis, feugiat a, tellus. Phasellus viverra nulla ut metus varius laoreet. Quisque rutrum. Aenean imperdiet. Etiam ultricies nisi vel</p>
    <p>augue. Curabitur ullamcorper ultricies nisi. Nam eget dui. Etiam rhoncus. Maecenas tempus, tellus eget condimentum rhoncus, sem quam semper libero, sit amet adipiscing sem neque sed ipsum. Nam quam nunc, blandit vel, luctus pulvinar, hendrerit id, lorem. Maecenas nec odio et ante tincidunt tempus. Donec vitae sapien ut libero venenatis faucibus. Nullam quis ante.</p>
  </section>

  <address class="contact">
    <div class="row company">
      <svg class="icon" width="10" height="13" viewBox="0 0 10 13" aria-hidden="true"><path d="M5 0.5a4.2 4.2 0 0 0-4.2 4.2C0.8 8 5 12.5 5 12.5S9.2 8 9.2 4.7A4.2 4.2 0 0 0 5 0.5z" fill="#6a5a48"/><circle cx="5" cy="4.6" r="1.6" fill="#f6ecc8"/></svg>
      Glaserei Velmar
    </div>
    <div class="row address">Birkenweg 12,<br>24100 Falkstedt</div>
    <div class="row mail">
      <svg class="icon" width="12" height="9" viewBox="0 0 12 9" aria-hidden="true"><rect x="0.5" y="0.5" width="11" height="8" fill="none" stroke="#6a5a48"/><path d="M0.5 0.5 6 5 11.5 0.5" fill="none" stroke="#6a5a48"/></svg>
      e-mail info@glaserei-velmar.example
    </div>
    <div class="row web">www.glaserei-velmar.example</div>
  </address>

  <div class="social">
    <div class="channel"><span class="square"></span>Bildnetz</div>
    <div class="channel"><span class="square"></span>Kontaktbuch</div>
  </div>

  <div class="brand-name">Glaserei Velmar</div>
</main>
</body>
</html>
```